Digitale Weihnachtskarte für Energieberater
Zielgruppe
Beratung in Bezug auf Energiemanagement/Energieeffizienz in Gebäuden
Gebäudetechnik
Kunden aufzeigen, wie Energie und somit Kosten gespart werden können
Zielgruppe: unsere Kunden, Interessenten und Lieferanten
Aufgabenstellung
Die digitale Weihnachtskarte wird schlussendlich per Mailing verschickt. Es wird eine jpg- und eine pdf-Datei benötigt.
Design:
Weihnachtliches, eher schlichtes Design. Letztjährige Projekte: #293721, #484192, #437447
Logo muss integriert werden, muss aber nicht im Vordergrund stehen.
Das Bild im Anhang kann, aber muss nicht verwendet werden.
Farbwahl:
Blau:
CMYK = 95/75/0/0
HEX = #244a9a
RGB = 36/74/154
Orange:
CMYK = 0/60/100/0
HEX = #ef7d00
RGB = 239/125/0
Grau:
CMYK = 0/0/0/65
HEX = #7c7c7b
RGB = 124/124/123
Grün:
CMYK = 60/100/0/0
HEX = #76b82a
RGB = 118/184/42
Schrift: DIN oder Arial, nicht kursiv
Geschätzte Kunden und Partner
Das Jahr neigt sich dem Ende zu und lädt uns dazu ein, auf das vergangene Jahr zurückzublicken, aber auch mit Zuversicht und frischem Elan in einen neuen Zeitabschnitt zu starten. Dank fortschrittlichen Technologien, Prozessoptimierungen und Investitionen wurde der Erfolg der vendralis Schweiz AG vorangetrieben. Mit unserem neuen Standort in Stuttgart haben wir einen weiteren Meilenstein gelegt.
Dankbar dafür, dass wir mit Ihnen zusammen in die Zukunft weiterschreiten dürfen, wünschen wir Ihnen und Ihrer Familie eine entspannte und besinnliche Weihnachtszeit und ein glückliches neues Jahr!

```html
<!DOCTYPE html>
<html lang="de">
<head>
<meta charset="utf-8">
<title>Weihnachtskarte vendralis</title>
<link rel="stylesheet" href="https://fonts.googleapis.com/css2?family=Arimo:wght@400;700&family=Pinyon+Script&display=swap">
<style>
  :root {
    --stage: #dfe0e4;
    --navy: #1f2448;
    --paper: #fdfdfb;
    --brand-blue: #244a9a;
    --ink: #2a3163;
    --silver: #8c8c92;
    --white: #ffffff;
  }
  * { margin: 0; padding: 0; box-sizing: border-box; }
  html, body { width: 1200px; height: 1200px; overflow: hidden; background: var(--stage); }
  .canvas { position: relative; width: 1200px; height: 1200px; font-family: "Arimo", Arial, sans-serif; }
  .panel { position: absolute; width: 548px; height: 548px; }

  /* Front: star tree */
  .front { left: 40px; top: 52px; background: var(--navy); }
  .front svg { position: absolute; inset: 0; }
  .greeting-word {
    position: absolute;
    font-family: "Pinyon Script", cursive;
    font-size: 27px;
    color: var(--silver);
    line-height: 1;
  }

  /* Back: logo and addresses */
  .back { left: 616px; top: 52px; width: 550px; height: 550px; background: var(--navy); padding: 19px; }
  .back-inner { width: 100%; height: 100%; background: var(--paper); position: relative; color: var(--ink); text-align: center; }
  .brand { position: absolute; left: 0; right: 0; top: 112px; display: flex; justify-content: center; align-items: center; gap: 10px; }
  .brand-name { font-size: 38px; font-weight: 400; color: var(--brand-blue); letter-spacing: 0.5px; }
  .brand-dot { width: 34px; height: 34px; border-radius: 50%; background: var(--brand-blue); }
  .address { position: absolute; left: 0; right: 0; font-size: 12.5px; line-height: 15.6px; }
  .address.main { top: 285px; }
  .address.branch { top: 371px; }
  .web { position: absolute; left: 0; right: 0; top: 466px; font-size: 12.5px; }

  /* Inside: letter */
  .inside {
    left: 40px; top: 620px;
    background: radial-gradient(ellipse at 50% 50%, #222851 0%, var(--navy) 70%);
    color: var(--white);
  }
  .letter { position: absolute; left: 0; right: 0; top: 121px; text-align: center; font-size: 14.4px; line-height: 16px; }
  .letter p { margin-bottom: 16px; }
</style>
</head>
<body>
<div class="canvas">

  <section class="panel front">
    <svg width="548" height="548" viewBox="0 0 548 548" role="img" aria-label="Weihnachtsbaum aus silbernen Sternen mit einem Stern an der Spitze">
      <defs>
        <linearGradient id="tree-tone" x1="0" y1="0" x2="0" y2="1">
          <stop offset="0" stop-color="#8c8c92" stop-opacity="0.35"/>
          <stop offset="1" stop-color="#8c8c92" stop-opacity="0.18"/>
        </linearGradient>
      </defs>
      <polygon points="284,48 86,508 482,508" fill="url(#tree-tone)"/>
    </svg>
    <span class="greeting-word" style="left:196px;top:148px">Frohes</span>
    <span class="greeting-word" style="left:300px;top:222px">neues</span>
    <span class="greeting-word" style="left:128px;top:343px">Jahr</span>
    <span class="greeting-word" style="left:352px;top:343px">Frohe</span>
    <span class="greeting-word" style="left:98px;top:458px">Weihnachten</span>
  </section>

  <section class="panel back">
    <div class="back-inner">
      <div class="brand">
        <span class="brand-name">vendralis</span>
        <span class="brand-dot"></span>
      </div>
      <div class="address main">
        vendralis Schweiz AG<br>
        Lindenweg 12<br>
        4600 Olten<br>
        Tel. +41 62 555 18 40
      </div>
      <div class="address branch">
        vendralis Schweiz AG<br>
        Niederlassung Deutschland<br>
        Gewerbepark 9<br>
        70563 Stuttgart<br>
        Tel. +49 711 20931 500
      </div>
      <div class="web">www.vendralis.com</div>
    </div>
  </section>

  <section class="panel inside" role="img" aria-label="Nachthimmel mit funkelnden Sternen">
    <div class="letter">
      <p>Geschätzte Kunden und Partner</p>
      <p>Das Jahr neigt sich dem Ende zu und lädt uns dazu ein,<br>
      auf das vergangene Jahr zurückzublicken, aber auch mit<br>
      Zuversicht und frischem Elan in einen neuen Zeitabschnitt<br>
      zu starten. Dank fortschrittlichen Technologien,<br>
      Prozessoptimierungen und Investitionen wurde der Erfolg<br>
      der vendralis Schweiz AG vorangetrieben. Mit unserem<br>
      neuen Standort in Stuttgart haben wir einen weiteren<br>
      Meilenstein gelegt.</p>
      <p>Dankbar dafür, dass wir mit Ihnen zusammen in die Zukunft<br>
      weiterschreiten dürfen, wünschen wir Ihnen und Ihrer Familie<br>
      eine entspannte und besinnliche Weihnachtszeit und ein<br>
      glückliches neues Jahr!</p>
      <p>Ihr vendralis-Team</p>
    </div>
  </section>

</div>
</body>
</html>
```